Update our OBGYN business card look and info

We are an OBGYN office. Our logo is nice but would like to "woman" part of the logo to be a darker color, to contrast with the flower that surrounds it. Maybe make our practice name Bloom Circle Health more feminine. Our practice caters to women only. All providers and staff are female.

Target Market(s)

Females 16-65.

Industry/Entity Type

Business

Contact Information for Business Card

See attached upload. The ONLY CHANGE to the information is DELETE the name Marla Quenbright, Midwife and REPLACE with Tessa Dravinoux, Midwife

Logo Text

Bloom Circle Health Obstetrics & Gynecology

Font styles to use
Serif
Script

Colors
85cae6
0692cd
33a6d7
85abd2
f59195
eea4c8
cadf82
fac994
d3a5cc

```html
<!DOCTYPE html>
<html lang="en">
<head>
<meta charset="utf-8">
<title>Bloom Circle Health – Business Card</title>
<link href="https://fonts.googleapis.com/css2?family=Marcellus&family=Arimo:wght@400;700&display=swap" rel="stylesheet">
<style>
  :root {
    --backdrop: #1f1f21;
    --card-dark: #4a4a4d;
    --card-dark-deep: #3c3c3f;
    --card-light: #f4f4f4;
    --teal: #85cae6;
    --teal-strong: #6fb8d4;
    --ink: #3d3d40;
    --white: #ffffff;
  }
  * { box-sizing: border-box; margin: 0; padding: 0; }
  html, body { width: 1200px; height: 800px; overflow: hidden; }
  body {
    background: var(--backdrop);
    font-family: "Arimo", Arial, sans-serif;
    position: relative;
  }
  .card {
    position: absolute;
    width: 600px;
    height: 340px;
    left: 300px;
    overflow: hidden;
    box-shadow: 0 10px 30px rgba(0,0,0,.5);
  }
  /* Front */
  .card-front {
    top: 40px;
    background: radial-gradient(ellipse at 30% 30%, var(--card-dark), var(--card-dark-deep));
  }
  .faint-circle {
    position: absolute;
    width: 300px; height: 300px;
    right: -60px; top: 40px;
    border-radius: 50%;
    background: rgba(255,255,255,.05);
  }
  .front-lockup {
    position: absolute;
    left: 0; right: 0; top: 110px;
    display: flex; justify-content: center; align-items: center; gap: 16px;
    color: var(--white);
  }
  .lockup-dot {
    width: 46px; height: 46px; border-radius: 50%;
    background: var(--white);
  }
  .lockup-name {
    font-family: "Marcellus", Georgia, serif;
    font-size: 21px; letter-spacing: .5px; text-transform: uppercase; line-height: 1.2;
  }
  .lockup-tag {
    font-family: "Marcellus", Georgia, serif;
    font-size: 21px; letter-spacing: .5px;
  }
  .front-web {
    position: absolute; left: 0; right: 0; top: 252px;
    text-align: center; color: var(--white);
    font-size: 13px; letter-spacing: 2px;
  }
  /* Back */
  .card-back {
    top: 420px;
    background: var(--card-light);
  }
  .back-wave { position: absolute; inset: 0; }
  .back-lockup {
    position: absolute; left: 56px; top: 34px;
    font-family: "Marcellus", Georgia, serif;
    color: var(--teal-strong);
    font-size: 18px; line-height: 1.25;
  }
  .back-lockup .lockup-name { font-size: 18px; }
  .back-lockup .lockup-tag { font-size: 18px; }
  .providers {
    position: absolute; left: 40px; top: 108px;
    list-style: none; color: var(--ink);
    font-size: 14px; line-height: 18px;
  }
  .providers strong { font-weight: 700; }
  .back-web {
    position: absolute; left: 30px; top: 298px;
    color: var(--white); font-size: 14px;
  }
  .back-web b { color: var(--teal); }
  .office {
    position: absolute; right: 30px; top: 226px;
    text-align: right; color: var(--white);
    font-size: 12px; line-height: 15px; font-style: normal;
  }
  .office-name { color: var(--teal); font-weight: 700; font-size: 13px; }
  .office-rule {
    width: 36px; height: 2px; background: var(--teal);
    margin: 6px 0 4px auto;
  }
  .contact-line { display: flex; justify-content: flex-end; align-items: center; gap: 8px; }
  .contact-line svg { width: 11px; height: 11px; }
</style>
</head>
<body>

<section class="card card-front">
  <div class="faint-circle"></div>
  <div class="front-lockup">
    <span class="lockup-dot"></span>
    <div>
      <div class="lockup-name">Bloom Circle Health</div>
      <div class="lockup-tag">Obstetrics &amp; Gynecology</div>
    </div>
  </div>
  <div class="front-web">www.bloomcircle.example</div>
</section>

<section class="card card-back">
  <svg class="back-wave" viewBox="0 0 600 340" preserveAspectRatio="none">
    <path d="M0,200 C60,278 200,300 300,262 L300,268 C200,306 60,292 0,236 Z" fill="var(--teal)"/>
    <path d="M0,236 C70,296 200,300 300,262 C380,232 470,150 600,140 L600,340 L0,340 Z" fill="var(--card-dark)"/>
    <path d="M420,206 C480,172 540,156 592,152" fill="none" stroke="var(--white)" stroke-width="2.5" opacity=".9"/>
  </svg>

  <div class="back-lockup">
    <div class="lockup-name">Bloom Circle Health</div>
    <div class="lockup-tag">Obstetrics &amp; Gynecology</div>
  </div>

  <ul class="providers">
    <li><strong>Renata Vollick,</strong> MD</li>
    <li><strong>Dana Pirswell,</strong> MD</li>
    <li><strong>Ines Marlow,</strong> MD</li>
    <li><strong>Tessa Dravinoux,</strong> Midwife</li>
    <li><strong>Sylvie Ardenholt,</strong> Midwife</li>
  </ul>

  <div class="back-web">www.<b>bloomcircle</b>.example</div>

  <address class="office">
    <div class="office-name">Bloom Circle Health</div>
    <div>418 Larkspur Avenue</div>
    <div>Suite 3B, Fairhollow, GA 30999</div>
    <div class="office-rule"></div>
    <div class="contact-line">(555) 014-2287
      <svg viewBox="0 0 12 12"><path d="M2.5 1 L4.5 1 L5.2 3.5 L4 4.6 C4.7 6 6 7.3 7.4 8 L8.5 6.8 L11 7.5 L11 9.5 C11 10.3 10.3 11 9.5 11 C5 11 1 7 1 2.5 C1 1.7 1.7 1 2.5 1 Z" fill="var(--teal)"/></svg>
    </div>
    <div class="contact-line">(555) 014-2290
      <svg viewBox="0 0 12 12"><rect x="3" y="1" width="6" height="3" fill="var(--teal)"/><rect x="1" y="4.5" width="10" height="4.5" rx="1" fill="var(--teal)"/><rect x="3" y="8" width="6" height="3" fill="var(--white)" stroke="var(--teal)"/></svg>
    </div>
    <div class="contact-line">hello@bloomcircle.example
      <svg viewBox="0 0 12 12"><rect x="1" y="2.5" width="10" height="7" fill="none" stroke="var(--teal)" stroke-width="1.2"/><path d="M1 2.5 L6 7 L11 2.5" fill="none" stroke="var(--teal)" stroke-width="1.2"/></svg>
    </div>
  </address>
</section>

</body>
</html>
```